Marlow Optics PowerPoint Template

Marlow Optics needs a nice new corporate PowerPoint template, to be used for all types of presentations: sales, business development, finance, board/exec, etc.

I'd like to get a clean layout that reflects the brand (www.marlowoptics.example), has a bright, interesting title slide, and then minimal graphics on the content slides. Ideally the content slides would have a header, "mo" circle part of the Marlow Optics logo (either above or below), copyright/confidential footer, and page #.

About us: we have developed a revolutionary new array camera for mobile devices, providing depth at every pixel. Focus on any subject, change focus (even on multiple subjects) after you take the photo, capture linear measurements, scale and segment your images, change backgrounds, and apply filters, all from any device.
It's not just about megapixels anymore.
See www.marlowoptics.example for info.

Target Market(s)

The audience for 90% of our presentations is highly educated executives at technology companies.

Industry/Entity Type

Camera

Requirements
Nice to have
• It would be great to show an image in a phone UI on the title slide, similar to the approach on our website.
Helpful to have tagline on title slide: "A smart camera for your smartphone." It may also fit on the content slides - feel free to try.
I attached a product photo, but using it is completely optional.
I'd like the "mo" circle on the content slides, but the whole logo on the title slides.
Thanks!

```html
<!DOCTYPE html>
<html lang="en">
<head>
<meta charset="utf-8">
<title>Marlow Optics – About Resolution</title>
<link href="https://fonts.googleapis.com/css2?family=Exo+2:wght@400&family=Open+Sans:wght@400;600&family=Archivo+Narrow:wght@700&display=swap" rel="stylesheet">
<style>
  :root {
    --ink: #333638;
    --brand-blue: #1b6a8c;
    --brand-navy: #0e3b55;
    --body-text: #3c3f41;
    --header-top: #f7f7f8;
    --header-bottom: #e3e3e5;
    --footer-band: #555a5a;
    --footer-rule: #d5d7d7;
    --white: #ffffff;
  }
  * { box-sizing: border-box; margin: 0; padding: 0; }
  html, body { width: 1200px; height: 900px; overflow: hidden; background: var(--white); }
  .slide { position: relative; width: 1200px; height: 900px; overflow: hidden; background: var(--white); font-family: "Open Sans", sans-serif; }

  .slide-header {
    position: absolute; left: 0; top: 0; width: 1200px; height: 99px;
    background: linear-gradient(to bottom, var(--header-top), var(--header-bottom));
  }
  .slide-title {
    position: absolute; left: 44px; top: 26px;
    font-family: "Exo 2", sans-serif; font-weight: 400; font-size: 39px; line-height: 1;
    color: var(--ink);
  }
  .slide-title .accent { color: var(--brand-blue); }
  .brand-name {
    position: absolute; right: 40px; top: 36px;
    display: flex; align-items: center; gap: 10px;
    font-family: "Open Sans", sans-serif; font-weight: 600; font-size: 22px; line-height: 28px;
    color: var(--brand-navy);
  }
  .brand-dot { width: 18px; height: 18px; border-radius: 50%; background: var(--brand-navy); }

  .backdrop-texture {
    position: absolute; left: 620px; top: 99px; width: 580px; height: 640px;
    background: radial-gradient(ellipse at 85% 30%, rgba(220,222,225,0.55), rgba(255,255,255,0) 65%);
  }

  .topic { position: absolute; left: 53px; }
  .topic-icon { position: absolute; left: 0; top: 0; }
  .topic-heading {
    position: absolute; left: 65px; top: 4px; white-space: nowrap;
    font-size: 24.5px; font-weight: 400; color: var(--body-text); line-height: 36px;
  }
  .point { position: absolute; left: 120px; width: 880px; }
  .point-chevron { position: absolute; left: 0; top: 9px; }
  .point-text {
    position: absolute; left: 24px; top: 0; width: 840px;
    font-size: 19.5px; font-weight: 600; line-height: 29px; color: var(--body-text);
  }

  .footer-rule { position: absolute; left: 0; top: 837px; width: 1200px; height: 9px; background: var(--footer-rule); }
  .slide-footer {
    position: absolute; left: 0; top: 846px; width: 1200px; height: 54px; background: var(--footer-band);
    font-family: "Archivo Narrow", sans-serif; font-weight: 700; font-size: 21px; color: var(--white);
    letter-spacing: 0.5px;
  }
  .page-number { position: absolute; left: 48px; top: 13px; }
  .copyright { position: absolute; right: 48px; top: 13px; }
</style>
</head>
<body>
<main class="slide">
  <header class="slide-header">
    <h1 class="slide-title">About <span class="accent">Resolution</span></h1>
    <div class="brand-name"><span class="brand-dot" aria-hidden="true"></span>Marlow Optics</div>
  </header>

  <div class="backdrop-texture" role="img" aria-label="Soft dotted texture fading across the right of the slide"></div>

  <section class="topic" style="top:164px;">
    <svg class="topic-icon" width="44" height="44" viewBox="0 0 44 44" aria-hidden="true">
      <circle cx="22" cy="22" r="21" fill="#e6e7e8"/>
      <circle cx="22" cy="22" r="16" fill="var(--brand-navy)"/>
      <path d="M13 22h16M23 16l6 6-6 6" stroke="#fff" stroke-width="3" fill="none" stroke-linecap="round" stroke-linejoin="round"/>
    </svg>
    <h2 class="topic-heading">Lorem ipsum dolor sit ipsum Lorem ipsum dolor sit ipsum Lorem ipsum</h2>
  </section>

  <div class="point" style="top:223px;">
    <svg class="point-chevron" width="12" height="14" viewBox="0 0 12 14" aria-hidden="true"><path d="M2 1l7 6-7 6" stroke="var(--brand-navy)" stroke-width="3.2" fill="none"/></svg>
    <p class="point-text">Lorem ipsum dolor sit ipsum Lorem ipsum dolor sit ipsum Lorem ipsum&nbsp; Lorem ipsum dolor sit ipsum Lorem ipsum dolor sit ipsum Lorem ipsum</p>
  </div>
  <div class="point" style="top:310px;">
    <svg class="point-chevron" width="12" height="14" viewBox="0 0 12 14" aria-hidden="true"><path d="M2 1l7 6-7 6" stroke="var(--brand-navy)" stroke-width="3.2" fill="none"/></svg>
    <p class="point-text">Lorem ipsum dolor sit ipsum Lorem ipsum dolor sit ipsum Lorem ipsum&nbsp; Lorem ipsum dolor sit ipsum Lorem ipsum dolor sit ipsum Lorem ipsum</p>
  </div>
  <div class="point" style="top:397px;">
    <svg class="point-chevron" width="12" height="14" viewBox="0 0 12 14" aria-hidden="true"><path d="M2 1l7 6-7 6" stroke="var(--brand-navy)" stroke-width="3.2" fill="none"/></svg>
    <p class="point-text">Lorem ipsum dolor sit ipsum Lorem ipsum dolor sit ipsum Lorem ipsum&nbsp; Lorem ipsum dolor sit ipsum Lorem ipsum dolor sit ipsum Lorem ipsum</p>
  </div>

  <section class="topic" style="top:479px;">
    <svg class="topic-icon" width="44" height="44" viewBox="0 0 44 44" aria-hidden="true">
      <circle cx="22" cy="22" r="21" fill="#e6e7e8"/>
      <circle cx="22" cy="22" r="16" fill="var(--brand-navy)"/>
      <path d="M13 22h16M23 16l6 6-6 6" stroke="#fff" stroke-width="3" fill="none" stroke-linecap="round" stroke-linejoin="round"/>
    </svg>
    <h2 class="topic-heading">Lorem ipsum dolor sit ipsum Lorem ipsum dolor sit ipsum Lorem ipsum</h2>
  </section>

  <div class="point" style="top:538px;">
    <svg class="point-chevron" width="12" height="14" viewBox="0 0 12 14" aria-hidden="true"><path d="M2 1l7 6-7 6" stroke="var(--brand-navy)" stroke-width="3.2" fill="none"/></svg>
    <p class="point-text">Lorem ipsum dolor sit ipsum Lorem ipsum dolor sit ipsum Lorem ipsum&nbsp; Lorem ipsum dolor sit ipsum Lorem ipsum dolor sit ipsum Lorem ipsum</p>
  </div>
  <div class="point" style="top:625px;">
    <svg class="point-chevron" width="12" height="14" viewBox="0 0 12 14" aria-hidden="true"><path d="M2 1l7 6-7 6" stroke="var(--brand-navy)" stroke-width="3.2" fill="none"/></svg>
    <p class="point-text">Lorem ipsum dolor sit ipsum Lorem ipsum dolor sit ipsum Lorem ipsum&nbsp; Lorem ipsum dolor sit ipsum Lorem ipsum dolor sit ipsum Lorem ipsum</p>
  </div>
  <div class="point" style="top:712px;">
    <svg class="point-chevron" width="12" height="14" viewBox="0 0 12 14" aria-hidden="true"><path d="M2 1l7 6-7 6" stroke="var(--brand-navy)" stroke-width="3.2" fill="none"/></svg>
    <p class="point-text">Lorem ipsum dolor sit ipsum Lorem ipsum dolor sit ipsum Lorem ipsum&nbsp; Lorem ipsum dolor sit ipsum Lorem ipsum dolor sit ipsum Lorem ipsum</p>
  </div>

  <div class="footer-rule"></div>
  <footer class="slide-footer">
    <span class="page-number">Page No. 00</span>
    <span class="copyright">Copyright@2013</span>
  </footer>
</main>
</body>
</html>
```